Business card design needed for Automotive Reconditioning business

I have a logo design i just cant decide on the best color or layout for the business card, I will upload all the files so you can see all colors schemes we are considering. I have other file formats if needed let me know.

Target Market(s)

automotive dealerships

Contact Information for Business Card

HERE are the Descriptions and info needed on the card:
Interior Repair: Leather carpet burns panels dash Deoderize
Dealer products and Vin Verify
( spot for name and cell number) My name is Norman Bexley phone 614 352-4180 Title COO www.QuorvalMotive.com

Font styles to use
Sans Serif
Other font styles liked:
• what ever you think looks best

Requirements
Must have
• Must be able to change the name and phone for employees

```html
<!DOCTYPE html>
<html lang="en">
<head>
<meta charset="utf-8">
<title>Quorval Motive – Business Card</title>
<link rel="stylesheet" href="https://fonts.googleapis.com/css2?family=Roboto:wght@400;500;700&display=swap">
<style>
  :root {
    --stage: #9a9a9a;
    --navy: #284b89;
    --red: #e8372c;
    --white: #ffffff;
    --ink: #2a2a2a;
    --muted: #555a63;
    --rule: #2d4f8e;
  }
  * { margin: 0; padding: 0; box-sizing: border-box; }
  html, body { width: 1200px; height: 930px; overflow: hidden; }
  body {
    background: var(--stage);
    font-family: "Roboto", Arial, sans-serif;
    position: relative;
  }
  .card {
    position: absolute;
    width: 600px;
    height: 343px;
    border-radius: 22px;
    overflow: hidden;
    box-shadow: 0 10px 24px rgba(0,0,0,.25);
  }
  .card--front { left: 80px; top: 80px; background: var(--navy); }
  .card--back { left: 520px; top: 507px; background: var(--white); }

  .brand {
    position: absolute;
    display: flex;
    align-items: center;
    gap: 10px;
    font-weight: 700;
    letter-spacing: .5px;
    text-transform: uppercase;
    white-space: nowrap;
  }
  .brand__dot { border-radius: 50%; flex: none; }
  .card--front .brand {
    left: 50%; top: 50%;
    transform: translate(-50%, -50%);
    font-size: 38px;
    color: var(--white);
  }
  .card--front .brand__dot { width: 22px; height: 22px; background: var(--red); }
  .card--back .brand {
    right: 34px; top: 38px;
    font-size: 24px;
    color: var(--navy);
  }
  .card--back .brand__dot { width: 14px; height: 14px; background: var(--red); }

  .divider {
    position: absolute;
    left: 34px; right: 34px; top: 118px;
    height: 1px;
    background: var(--rule);
  }
  .person { position: absolute; left: 40px; top: 136px; }
  .person__name {
    font-size: 26px;
    font-weight: 500;
    color: var(--navy);
    text-transform: uppercase;
    white-space: nowrap;
  }
  .person__title {
    font-size: 15px;
    color: var(--muted);
    margin-top: 2px;
    margin-left: 6px;
  }
  .person__rule {
    width: 250px; height: 1.5px;
    background: var(--rule);
    margin-top: 10px;
  }
  .contacts { position: absolute; left: 44px; top: 226px; list-style: none; }
  .contacts li {
    display: flex; align-items: center; gap: 10px;
    font-size: 15px; color: var(--ink);
    line-height: 23px;
    white-space: nowrap;
  }
  .contacts svg { width: 11px; height: 11px; fill: var(--navy); flex: none; }
  .contacts .web strong { color: var(--navy); font-weight: 500; }

  .address {
    position: absolute;
    right: 40px; top: 158px;
    text-align: right;
    font-size: 14px;
    line-height: 20px;
    color: var(--ink);
    font-style: normal;
    white-space: nowrap;
  }
  .wave { position: absolute; left: 0; bottom: 0; width: 600px; height: 130px; }
</style>
</head>
<body>

<section class="card card--front" aria-label="Card front">
  <div class="brand"><span class="brand__dot"></span>Quorval Motive</div>
</section>

<section class="card card--back" aria-label="Card back">
  <div class="brand"><span class="brand__dot"></span>Quorval Motive</div>
  <div class="divider"></div>

  <div class="person">
    <div class="person__name">Norman Bexley</div>
    <div class="person__title">COO</div>
    <div class="person__rule"></div>
  </div>

  <ul class="contacts">
    <li><svg viewBox="0 0 24 24"><path d="M6.6 10.8a15 15 0 0 0 6.6 6.6l2.2-2.2c.3-.3.7-.4 1-.2 1.1.4 2.3.6 3.6.6.6 0 1 .4 1 1V20c0 .6-.4 1-1 1A17 17 0 0 1 3 4c0-.6.4-1 1-1h3.5c.6 0 1 .4 1 1 0 1.3.2 2.5.6 3.6.1.3 0 .7-.2 1z"/></svg>614 352-4180</li>
    <li><svg viewBox="0 0 24 24"><path d="M2 5h20v14H2zm2 2v.5l8 5 8-5V7zm0 3v7h16v-7l-8 5z"/></svg>info@quorvalmotive.com</li>
    <li class="web"><svg viewBox="0 0 24 24"><path d="M12 2a10 10 0 1 0 0 20 10 10 0 0 0 0-20zm6.9 6h-3a15 15 0 0 0-1.3-3.9A8 8 0 0 1 18.9 8zM12 4c.8 1.2 1.5 2.5 1.9 4h-3.8c.4-1.5 1.1-2.8 1.9-4zM4.3 14a8 8 0 0 1 0-4h3.4a16 16 0 0 0 0 4zm.8 2h3a15 15 0 0 0 1.3 3.9A8 8 0 0 1 5.1 16zM8 8H5.1a8 8 0 0 1 4.3-3.9C8.8 5.3 8.4 6.6 8 8zm4 12c-.8-1.2-1.5-2.5-1.9-4h3.8c-.4 1.5-1.1 2.8-1.9 4zm2.3-6H9.7a14 14 0 0 1 0-4h4.6a14 14 0 0 1 0 4zm.3 5.9c.6-1.2 1-2.5 1.3-3.9h3a8 8 0 0 1-4.3 3.9zm1.7-5.9a16 16 0 0 0 0-4h3.4a8 8 0 0 1 0 4z"/></svg>www.<strong>QuorvalMotive</strong>.com</li>
  </ul>

  <address class="address">512b Harlow Street,<br>Ashbury, NZ, 7042</address>

  <svg class="wave" viewBox="0 0 600 130" preserveAspectRatio="none" aria-hidden="true">
    <path d="M0 130 L0 128 C360 127 380 14 600 9 L600 130 Z" fill="var(--navy)"/>
    <path d="M0 125 C360 124 380 11 600 6" fill="none" stroke="var(--white)" stroke-width="5"/>
    <path d="M0 122 C360 121 380 8 600 3" fill="none" stroke="var(--red)" stroke-width="3"/>
  </svg>
</section>

</body>
</html>
```